Helicopter Company - Rotavia Sweden

I need a new design and implementation of a webpage. We rent helicopters and are also starting a school. We havre started a wordpress but the page is very ugly. Need a complete update. Logo exist already. We also have some pictures of helicotopers. We are open for all designs but it is important that it looks professionel, is eassy to update and will give an impression och structure and dicipline.
Updates

Target Market(s)

Customers that what to get a certificate to fly. It is expensive so it’s either people with a lot of money or people with a big dream. It is very serious business.

Industry/Entity Type

www.rotavia-demo.se

Coding

Coded - Design and coding required

Number of Pages Required

4 page

Font styles to use
Sans Serif

Colors
0054AA
0677BA
7BADD7
CADEEF
E8F1F8

Requirements
Must have
• A easy page the gives a feeling of seriousness and

```html
<!DOCTYPE html>
<html lang="sv">
<head>
<meta charset="utf-8">
<title>Rotavia – Hyr din helikopter</title>
<link rel="stylesheet" href="https://fonts.googleapis.com/css2?family=Lato:ital,wght@0,300;0,400;0,700;1,400&display=swap">
<style>
:root{
  --navy:#0a3a5c;
  --brand:#0a5f8c;
  --brand-strong:#0677BA;
  --footer:#0a6494;
  --frame:#7BADD7;
  --pale:#CADEEF;
  --mist:#E8F1F8;
  --ink:#2b2b2b;
  --white:#ffffff;
  --ghost:#ececec;
}
*{margin:0;padding:0;box-sizing:border-box}
html,body{width:1200px;height:2210px;overflow:hidden;background:var(--white)}
body{position:relative;font-family:'Lato',sans-serif;color:var(--ink)}
.abs{position:absolute}

/* hero */
.hero{left:0;top:0;width:1200px;height:835px;
  background:linear-gradient(180deg,#173f5c 0%,#3e6782 18%,#8a97a0 32%,#4d6b80 42%,#123349 58%,#0e2638 72%,#6d7c88 86%,#f4f6f8 96%,#fff 100%)}
.hero-photo{left:0;top:0;width:1200px;height:835px;
  background:radial-gradient(ellipse 260px 300px at 600px 560px,rgba(10,14,20,.75),transparent 70%),
             radial-gradient(ellipse 260px 220px at 1120px 580px,rgba(170,160,150,.45),transparent 70%)}
.logo{font-family:'Lato',sans-serif;font-weight:400;letter-spacing:3px;color:var(--white)}
.nav-logo{left:120px;top:24px;font-size:34px}
.nav{top:28px;font-size:12px;color:var(--white)}
.hero-title{left:0;width:1200px;top:312px;text-align:center;font-size:54px;font-weight:400;color:var(--white)}
.hero-sub{left:0;width:1200px;top:386px;text-align:center;font-size:26px;font-weight:300;color:var(--white)}
.hero-btn{left:519px;top:538px;width:161px;height:46px;border-radius:4px;background:var(--brand);
  color:var(--white);font-size:13px;display:flex;align-items:center;justify-content:center}

/* about */
.about-ghost{left:118px;top:840px;font-size:100px;font-weight:700;color:var(--ghost);letter-spacing:-2px;line-height:1}
.about-frame{left:120px;top:905px;width:275px;height:396px;border:3px solid var(--frame)}
.about-photo{left:283px;top:930px;width:225px;height:347px;
  background:linear-gradient(180deg,#0b3f86 0%,#3f86c8 40%,#a9c6dc 62%,#8f8578 78%,#6b6258 100%);
  box-shadow:0 6px 14px rgba(0,0,0,.25)}
.about-label{left:134px;font-size:11.5px}
.about-label.blue{color:var(--brand)}
.tag-block{left:134px;width:124px;font-size:9px;font-style:italic;line-height:12.5px;padding:0 2px}
.tag-block.dark{background:var(--brand);color:var(--white)}
.tag-block.light{background:var(--mist);color:var(--brand)}
.about-kicker{left:610px;top:954px;font-size:27px;font-weight:400;color:var(--ink)}
.about-title{left:610px;top:993px;font-size:30px;font-weight:700;color:var(--brand)}
.about-text{left:610px;width:392px;font-size:13.3px;line-height:17.3px;color:#333}
.learn{left:610px;top:1270px;font-size:16px;font-style:italic;color:var(--brand)}

/* fleet */
.sky{left:0;top:1370px;width:1200px;height:510px;
  background:radial-gradient(ellipse 400px 140px at 200px 120px,#eef1f6,transparent 70%),
             radial-gradient(ellipse 500px 160px at 1000px 110px,#eef1f6,transparent 70%),
             radial-gradient(ellipse 700px 180px at 600px 420px,#e9edf4,transparent 70%),
             linear-gradient(180deg,#fff 0%,#f3f5f9 40%,#f3f5f9 85%,#fff 100%)}
.card{box-shadow:0 6px 16px rgba(0,0,0,.2)}
.card-band{height:35px;background:var(--brand);display:flex;align-items:center;justify-content:center;font-size:17px}
.card-photo{width:100%}
.card-info{left:636px;top:1467px;width:183px;height:272px;background:var(--brand);color:var(--white);padding:0 18px}
.card-info h3{position:absolute;left:29px;top:89px;font-size:16.5px;font-weight:400}
.card-info p{position:absolute;left:18px;top:130px;width:152px;font-size:8.6px;font-style:italic;line-height:12.5px}
.card-info .more{position:absolute;left:22px;top:236px;font-size:9px;font-style:italic;display:flex;align-items:center;gap:4px;border-bottom:1px solid var(--white);padding-bottom:1px}

/* footer */
.footer{left:0;top:1877px;width:1200px;height:333px;background:var(--footer);color:var(--white);overflow:hidden}
.footer-cloud{border-radius:50%;filter:blur(18px);background:rgba(255,255,255,.75)}
.footer-logo{left:118px;top:28px;font-size:22px}
.f-col{top:98px}
.f-col h4{font-size:17px;font-weight:400;margin-bottom:14px}
.f-col p{font-size:11px;line-height:18.5px}
.f-col .hours{font-size:14px;line-height:20px}
.contact-row{display:flex;align-items:center;gap:10px;font-size:11px}
.social{width:15px;height:15px;border:1.5px solid var(--white);border-radius:50%}
</style>
</head>
<body>

<!-- Hero -->
<div class="abs hero" role="img" aria-label="Vy från helikopterns cockpit över hav, kust och stad, med moln i förgrunden"></div>
<div class="abs hero-photo"></div>
<div class="abs logo nav-logo">ROTAVIA</div>
<div class="abs nav" style="left:773px">Start</div>
<div class="abs nav" style="left:855px">Om Oss</div>
<div class="abs nav" style="left:935px">Kontakt</div>
<svg class="abs" style="left:1018px;top:28px" width="14" height="14" viewBox="0 0 14 14"><circle cx="5.5" cy="5.5" r="4" fill="none" stroke="#fff" stroke-width="1.8"/><line x1="8.5" y1="8.5" x2="13" y2="13" stroke="#fff" stroke-width="2"/></svg>
<h1 class="abs hero-title">Valkommen till Rotavia</h1>
<p class="abs hero-sub">Hyr din helikopter av oss!</p>
<a class="abs hero-btn">Las mer om oss!</a>

<!-- About -->
<div class="abs about-ghost">OM OSS</div>
<div class="abs about-frame"></div>
<div class="abs about-label blue" style="top:1002px">Lorem ipsum dolor sit amet</div>
<div class="abs tag-block dark" style="top:1030px">Lorem ipsum dolor sit amet consectetur. Lorem commodo sed faucibus sit varius neque</div>
<div class="abs about-label" style="top:1090px">Lorem ipsum dolor sit amet</div>
<div class="abs tag-block light" style="top:1110px">Lorem ipsum dolor sit amet consectetur. Lorem commodo sed faucibus sit varius neque</div>
<div class="abs about-photo" role="img" aria-label="Vit helikopter parkerad på asfalt under blå himmel"></div>
<h2 class="abs about-kicker">Lorem ipsum dolor sit amet</h2>
<h2 class="abs about-title">Lorem ipsum dolor sit amet</h2>
<p class="abs about-text" style="top:1060px">Lorem ipsum dolor sit amet consectetur. Sem lobortis ut adipiscing id enim. Ultrices aliquam vitae in a. Amet donec proin massa euismod risus. Mi odio potenti urna dictumst vel tempor. Nisi volutpat et pulvinar ornare at auctor habitant id.</p>
<p class="abs about-text" style="top:1149px">Lorem ipsum dolor sit amet consectetur. Accumsan sem aliquet metus faucibus id. Orci nibh diam amet auctor suspendisse. Metus arcu tempor egestas mauris pulvinar mattis felis a. Eu urna elit nunc odio.</p>
<a class="abs learn">Lär dig mer <svg width="16" height="10" viewBox="0 0 16 10"><path d="M1 5h13M10 1l4 4-4 4" fill="none" stroke="#0a5f8c" stroke-width="1.6"/></svg></a>

<!-- Fleet -->
<div class="abs sky" role="img" aria-label="Mjuka vita moln mot ljus himmel"></div>
<div class="abs card" style="left:200px;top:1515px;width:157px;height:197px">
  <div class="card-band logo">ROTAVIA</div>
  <div class="card-photo" style="height:162px;background:linear-gradient(135deg,#4a3a2c,#7a6a58 50%,#3b2e22)" role="img" aria-label="Hammare och spik på träyta"></div>
</div>
<div class="abs card" style="left:819px;top:1515px;width:180px;height:197px">
  <div class="card-band logo">ROTAVIA</div>
  <div class="card-photo" style="height:162px;background:linear-gradient(180deg,#7fa8d8 0%,#c5d6e8 35%,#6d7a80 60%,#8c8f92 100%)" role="img" aria-label="Mörkblå helikopter och grön sportbil på racerbana"></div>
</div>
<div class="abs card" style="left:357px;top:1479px;width:279px;height:249px;background:linear-gradient(180deg,#8fb6e0 0%,#3e5a3a 28%,#4f7a36 55%,#6f8f42 100%)" role="img" aria-label="Mörkblå helikopter på en gräsmatta framför skog"></div>
<div class="abs card card-info">
  <h3>Våra Helikoptrar!</h3>
  <p>Vi hyr ut helikopter av märket Rotorverk R4. Falk 1 och Glid 2. De är identiska utvändigt men skiljer sig lite rent tekniskt. Den ena är från 2021 och den andra har några fler år på nacken. Klicka på bilden för att läsa mer!</p>
  <span class="more">Lär dig mer <svg width="14" height="8" viewBox="0 0 14 8"><path d="M1 4h11M9 1l3 3-3 3" fill="none" stroke="#fff" stroke-width="1.3"/></svg></span>
</div>

<!-- Footer -->
<footer class="abs footer">
  <div class="abs footer-cloud" style="left:920px;top:-20px;width:300px;height:140px" role="img" aria-label="Moln"></div>
  <div class="abs footer-cloud" style="left:-80px;top:190px;width:380px;height:180px" role="img" aria-label="Moln"></div>
  <div class="abs logo footer-logo">ROTAVIA</div>
  <div class="abs f-col" style="left:199px">
    <h4>Länkar</h4>
    <p>www.landningsplats-demo.se<br>www.rotorverk-demo.com<br>www.norrfalt-flygklubb.se/</p>
  </div>
  <div class="abs f-col" style="left:363px">
    <h4>Partners</h4>
    <p>Landplatta<br>NRA<br>Vinga</p>
  </div>
  <div class="abs f-col" style="left:527px">
    <h4>Öppetider</h4>
    <p>Måndag – Söndag:</p>
    <p class="hours">09:00 – 17:00</p>
    <p>Övrig tid enligt överenskommelse.</p>
  </div>
  <div class="abs f-col" style="left:771px">
    <h4>Kontaktinformation</h4>
    <p>Rotavia,Norrfälts Flygfält</p>
    <div class="contact-row" style="margin-top:22px">
      <svg width="14" height="14" viewBox="0 0 14 14"><path d="M3 1l2.5 3-1.5 1.5c1 2 2.5 3.5 4.5 4.5L10 8.5l3 2.5-1.5 2C6 13 1 8 1 2.5z" fill="#fff"/></svg>
      <span>+46 700 123 456</span>
    </div>
    <div class="contact-row" style="margin-top:10px">
      <svg width="14" height="11" viewBox="0 0 14 11"><rect x="0.5" y="0.5" width="13" height="10" fill="#fff"/><path d="M1 1l6 5 6-5" fill="none" stroke="#0a6494" stroke-width="1.3"/></svg>
      <span>info@rotavia-demo.se</span>
    </div>
    <div class="contact-row" style="margin-top:38px;gap:6px">
      <span class="social" aria-label="Sociala medier"></span><span class="social" aria-label="Sociala medier"></span>
    </div>
  </div>
</footer>

</body>
</html>
```